Flyer-Design - Coaching & Supervision für freib. Dipl.-Psychologin - BITTE KEINE WEITEREN DESINGS
Zielgruppe
--------- An alle, die überlegen mitzumachen - ich habe gerade als ungefähren Zeitplan, dass ich mich bis Donnerstag Abend (27.01.) entscheide, damit dann am Freitag (+evtl. Wochenende) noch Zeit für das Feintuning ist. -------------------
Ich bin Diplom-Psychologin und arbeite unter anderem freiberuflich als Coach und Supervisorin. Für diese Arbeit brauche ich einen Flyer. Ich habe bereits ein Konzept mit den Inhalten erstellt und brauche dafür nun ein professionelles Layout.
Aufgabenstellung
Anbei finden Sie das Konzept 1x als ppt (inklusive ausprobierter Alternativen zu den Fotos) und 1x als pdf.
Der Flyer hat als zentrales Thema „sich verändern / sich auf den Weg machen“ sowie die Analogie, dass ein gutes Coachinggespräch wie eine Bergtour ist.
Ich habe viel Vorarbeit gemacht (Inhalte stehen, Fotos sind recherchiert…) – sehr gerne können Sie sich kreativ ausleben und was völlig Neues / alles anders machen, es wäre aber auch ok, wenn das bereits Erarbeitete einfach graphisch aufgepimpt und professionalisiert wird.
Mein Wunsch: Ich weiß, dass der Flyer sehr voll ist. Aber ich möchte bewusst relativ viel Info dort unterbringen. Deshalb wäre es gut, wenn die Grafik des Flyers eine gewisse Leichtigkeit beinhaltet, die den vielen Text eher kaschiert. Also nicht zu verschnörkelt, sondern eher schlicht, hell und das Auge entlastend. Ich wünsche mir warme Farbtöne, die einladen und nicht zu kühl-modern wirken.
Logo:
Das Logo habe ich hier auf der Seite gestaltmarkt.de entwickeln lassen und habe alle Rechte daran. Es kann bei Bedarf auch angepasst werden.
Aktuell ist das Logo in grün, da ich dadurch den Naturbezug meiner Metapher mit aufgreife und weil die gerade entstehende Homepage, aktuell auch grün als Grundfarbe hat. Allerdings werde ich die Homepage auch noch professional überarbeiten lassen. Anbei einen Screenshot wie die Startseite der Homepage im Moment so ca. aussieht.
Bilder:
Die Fotos von mir hat ein Fotograf gemacht und ich darf sie verwenden.
Die Landschaftsbilder habe ich kostenlos und lizenzfrei von Lumora Bild ( https://bild.lumora-fotos.de/de/frei ) und von Fotelix ( https://fotelix-bilder.de/de/ ) heruntergeladen.
Falls Sie andere Bilder besser fänden und diese vorschlagen wollen, dann finden Sie weitere Details zu meinen Wünschen an die Bilder im Dokument „SelmK_AusschreibungDetails“
Die Landkarte ist ein Screenshot von KartoWeltNetz. Dort steht i..

```html
<!DOCTYPE html>
<html lang="de">
<head>
<meta charset="utf-8">
<title>Coaching &amp; Supervision – Faltflyer</title>
<link href="https://fonts.googleapis.com/css2?family=Alegreya:ital,wght@0,400;0,500;1,400&family=Alegreya+Sans:wght@400;500;700&display=swap" rel="stylesheet">
<style>
:root{
  --green:#4f7b2e;
  --green-dark:#3f6e27;
  --olive:#8fa56c;
  --sage:#e4e5d3;
  --sage-deep:#d7dac2;
  --orange:#e3a03f;
  --paper:#ffffff;
  --ink:#3a3a36;
  --bg:#ecebe7;
}
*{box-sizing:border-box;margin:0;padding:0}
html,body{width:1200px;height:960px;overflow:hidden;background:var(--bg)}
body{font-family:"Alegreya Sans",sans-serif;color:var(--ink);position:relative}
.serif{font-family:"Alegreya",serif}
.spread{position:absolute;left:20px;width:1160px;height:450px;display:flex;box-shadow:0 6px 18px rgba(0,0,0,.12);background:var(--paper)}
.spread--outer{top:16px}
.spread--inner{top:494px}
.panel{position:relative;width:386.67px;height:100%;overflow:hidden;background:var(--paper)}
.panel + .panel{border-left:1px solid #e8e8e2}
.img{position:absolute;display:block}
.abs{position:absolute}

/* About */
.about-tab{left:0;top:20px;width:44px;height:122px;background:var(--orange);color:#fff;display:flex;align-items:center;justify-content:center;z-index:2}
.about-tab span{writing-mode:vertical-rl;transform:rotate(180deg);font-family:"Alegreya",serif;font-size:15px;line-height:1.05;text-align:left}
.about-tab b{font-family:"Alegreya Sans",sans-serif;font-weight:700;font-size:11px;display:block}
.about-photo{left:44px;top:20px;width:122px;height:90px;background:linear-gradient(135deg,#6d6a62,#a38a78 55%,#3c3a36);z-index:2}
.about-box{left:44px;top:64px;width:316px;height:210px;background:var(--sage)}
.qual{left:62px;top:118px;width:290px}
.qual h4,.xp h4{color:var(--green);font-weight:500;font-size:10.5px;line-height:1.15;margin-top:7px}
.qual p,.xp p{font-size:8.4px;line-height:1.25}
.xp{left:62px;top:282px;width:300px}
.xp ul{list-style:none;margin-top:4px}
.xp li{font-size:8.4px;line-height:1.35}
.xp li::before{content:"• "}

/* Location */
.loc-box{left:16px;top:18px;width:352px;height:414px;background:var(--sage)}
.loc-title{left:16px;top:30px;width:352px;text-align:center;color:var(--green);font-size:16px}
.loc-sub{left:16px;top:52px;width:352px;text-align:center;font-size:9px}
.map{left:36px;top:70px;width:312px;height:222px;background:linear-gradient(160deg,#e3e0cf,#d3dbc0 50%,#e6dcc6)}
.tags{left:0;top:232px}
.tag{display:block;background:var(--orange);color:#fff;font-weight:500;font-size:9.5px;padding:4px 0;text-align:center;margin-bottom:6px}
.loc-text{left:40px;top:312px;width:304px;text-align:center;font-size:8.4px;line-height:1.3}
.contact{left:16px;top:360px;width:352px;text-align:center;font-size:9.5px;line-height:1.3}
.contact h4{font-family:"Alegreya",serif;font-weight:500;font-size:12px;margin-bottom:3px}

/* Cover */
.brand{display:flex;align-items:center;gap:6px;color:var(--green);font-family:"Alegreya",serif;font-size:14px}
.brand i{width:18px;height:18px;border-radius:50%;border:1.5px solid var(--green);display:block}
.cover .brand{right:22px;top:26px}
.cover-title{left:24px;top:72px;color:var(--green);font-size:22px}
.cover-sub{left:24px;top:102px;font-size:9.5px}
.cover-photo{left:16px;top:122px;width:354px;height:312px;background:linear-gradient(180deg,#4f7fba 0%,#9cb8d8 28%,#7ea24a 45%,#5d8a33 70%,#8c9f60 100%)}
.cover-q{left:16px;top:322px;width:250px;background:rgba(143,165,108,.92);color:#fff;font-size:9px;line-height:1.3;padding:6px 10px 6px 26px}
.cover-claim{left:196px;top:352px;width:150px;background:var(--orange);color:#fff;font-family:"Alegreya",serif;font-style:italic;font-size:11.5px;line-height:1.25;padding:5px 8px}

/* Inner left */
.hike-photo{left:20px;top:24px;width:366px;height:266px;background:linear-gradient(180deg,#c9cfcf 0%,#dfe1dc 45%,#8f9a5e 70%,#6f7d3f 100%)}
.hike-tag{left:0;top:20px;width:186px;background:var(--orange);color:#fff;font-family:"Alegreya",serif;font-style:italic;font-size:11px;line-height:1.15;padding:5px 8px;text-align:right}
.theme-box{left:30px;top:240px;width:124px;height:196px;background:var(--sage-deep);padding:8px 10px}
.theme-box h3{font-family:"Alegreya",serif;font-weight:500;font-size:12px;line-height:1.05;margin-bottom:4px}
.theme-box p{font-size:7.8px;line-height:1.25;margin-bottom:8px}
.way{left:172px;top:326px;width:190px;color:var(--orange);font-size:9.2px;line-height:1.22}
.way h3{font-family:"Alegreya",serif;font-weight:400;font-size:12.5px;margin-bottom:2px}

/* Inner middle */
.info-bg{left:40px;top:14px;width:346px;height:422px;background:var(--sage)}
.info{left:60px;width:300px}
.info h3{font-family:"Alegreya",serif;font-weight:400;font-size:12px;margin-bottom:4px}
.info p{font-size:8.2px;line-height:1.3}
.h-orange{color:var(--orange)}
.h-green{color:var(--green-dark)}
.tiles{left:60px;top:308px;display:grid;grid-template-columns:98px 98px;gap:10px}
.tile{height:58px;color:#fff;text-align:center;padding:6px 4px;font-size:7px;line-height:1.2}
.tile b{display:block;font-size:8px;margin-bottom:2px}
.tile--dark{background:var(--green)}
.tile--light{background:var(--olive)}

/* Inner right */
.mean-title{left:24px;top:28px;color:var(--green);font-size:12px}
.chips{left:24px;top:56px;display:flex;gap:8px}
.chip{background:var(--sage-deep);color:var(--green);font-size:7.6px;font-weight:500;text-align:center;line-height:1.1;padding:4px 6px}
.sprout{left:0;top:96px;width:236px;height:100px;background:linear-gradient(90deg,#2f3a22,#6a8b2e 55%,#3b4a24)}
.attitude{left:236px;top:90px;width:122px;height:112px;background:var(--green);color:#fff;padding:10px 10px;font-size:8px;line-height:1.25}
.attitude h4{font-size:10px;margin-bottom:4px;line-height:1.1}
.attitude ul{list-style:none}
.attitude li::before{content:"• "}
.tmpl{left:24px;top:216px;width:330px}
.tmpl h3{font-family:"Alegreya",serif;font-weight:400;color:var(--green);font-size:12px;margin-bottom:6px}
.tmpl p{font-size:8.2px;line-height:1.3}
.answer{left:24px;top:326px;width:346px;height:110px;background:var(--orange)}
.answer-txt{left:34px;top:336px;width:150px;color:#fff}
.answer-txt h3{font-family:"Alegreya",serif;font-weight:400;font-size:12px;line-height:1.15;margin-bottom:8px}
.answer-txt p{font-size:8.4px;line-height:1.25}
.portrait{left:200px;top:326px;width:150px;height:110px;background:linear-gradient(135deg,#b9c7cc,#e8ecec 50%,#8d9ea3)}
</style>
</head>
<body>

<section class="spread spread--outer">
  <article class="panel about">
    <div class="abs about-box"></div>
    <div class="abs about-tab"><span>Über mich<b>Selma Kranich</b></span></div>
    <div class="img about-photo" role="img" aria-label="Porträtfoto der Psychologin"></div>
    <div class="abs qual">
      <h4>Diplom-Psychologin</h4>
      <p>Schwerpunkte: Arbeits- und Organisationspsychologie;<br>Systemische Familienpsychologie</p>
      <h4>Zertifizierte Coachingausbildung</h4>
      <p>bei TIVA Nord-Süd e.V. – anerkannt von<br>EVSC (Europäischer Verband für Supervision und Coaching)</p>
      <h4>Staatlich zertifizierte<br>Entspannungspädagogin</h4>
      <h4>Kursleiterausbildung</h4>
      <p>(„Train the trainer“) zur Durchführung<br>von Gruppenleiterausbildungen</p>
    </div>
    <div class="abs xp">
      <h4>Berufserfahrung in der Wirtschaft,<br>im sozialen und im kirchlichen Bereich</h4>
      <ul>
        <li>internationaler Großkonzern</li>
        <li>Unternehmensberatung</li>
        <li>Entwicklungshilfe</li>
        <li>Betriebliche Sozialberatung (EAP)</li>
        <li>Berufliche Fortbildungszentren</li>
        <li>Krisenintervention</li>
      </ul>
      <h4>Internationale Erfahrung <span style="font-size:8px;color:var(--ink)">(Englisches Coaching)</span></h4>
      <p>• 2 Jahre Kanada + 1 Jahr Irland</p>
    </div>
  </article>

  <article class="panel location">
    <div class="abs loc-box"></div>
    <h2 class="abs loc-title serif" style="font-weight:400">Coaching vor Ort oder Online</h2>
    <p class="abs loc-sub">im Herzen der Altstadt am Lindenplatz</p>
    <div class="img map" role="img" aria-label="Stadtplan der Umgebung mit dem Praxisstandort"></div>
    <div class="abs tags">
      <span class="tag" style="width:160px">digital oder telefonisch</span>
      <span class="tag" style="width:218px">direkt in Ihrem beruflichen Umfeld</span>
      <span class="tag" style="width:200px">In der Natur und in Bewegung</span>
    </div>
    <p class="abs loc-text">Vielen Menschen fällt es leichter zu reden, wenn sie sich bewegen. Gerne führe ich Gespräche gemeinsam unterwegs in einem Park oder in der freien Natur. Wenn wir uns bewegen, bewegt sich auch etwas in uns.</p>
    <div class="abs contact">
      <h4>Kontakt</h4>
      <p>Selma Kranich<br>+49 (0)160 0000 12 34</p>
      <p style="margin-top:4px">kontakt@selmakranich.de<br>www.selmakranich.de</p>
    </div>
  </article>

  <article class="panel cover">
    <div class="abs brand"><i></i>Selma Kranich</div>
    <h1 class="abs cover-title serif" style="font-weight:500">Coaching &amp; Supervision</h1>
    <p class="abs cover-sub">Selma Kranich | Diplom Psychologin</p>
    <div class="img cover-photo" role="img" aria-label="Wanderweg über eine grüne Hügelkuppe unter blauem Himmel"></div>
    <p class="abs cover-q">Stehen Sie vor einer schwierigen Situation?<br>Wollen Sie etwas in Ihrem Leben verändern?<br>Sind Sie irgendwie unzufrieden?<br>Möchten Sie neue Wege gehen?</p>
    <p class="abs cover-claim">Ich mache mich mit<br>Ihnen auf den Weg!</p>
  </article>
</section>

<section class="spread spread--inner">
  <article class="panel journey">
    <div class="img hike-photo" role="img" aria-label="Zwei Wanderer steigen über eine Bergwiese"></div>
    <p class="abs hike-tag">Ein gutes Coachinggespräch ist<br>wie eine gemeinsame Bergtour…</p>
    <div class="abs theme-box">
      <h3>Sie bestimmen das Thema – Ihren Berg.</h3>
      <p>Sie bestimmen das Tempo. Sie entdecken Ihre eigenen Ressourcen während Sie sich Schritt für Schritt Ihrem Ziel nähern.</p>
      <p>Gemeinsam erkunden wir, welche Wege es zu Ihrem Ziel gibt. Ich begleite Sie auf allen Etappen. Ich helfe Ihnen, sich unterwegs zu orientieren.</p>
    </div>
    <div class="abs way">
      <h3>Wir gehen den Weg:</h3>
      mit Offenheit, mit Neugierde, mit einem Lachen, mit einem klaren Blick, mit Pausen, mit Ausdauer, mit Freude, mit Motivation, mit allen Sinnen und allen Emotionen.
    </div>
  </article>

  <article class="panel info-panel">
    <div class="abs info-bg"></div>
    <div class="abs info" style="top:28px">
      <h3 class="h-orange">Was ist Coaching &amp; Supervision?</h3>
      <p>Im Coaching und in der Supervision haben Sie die Möglichkeit, Ihr eigenes Handeln im beruflichen Kontext zu reflektieren. Mit Hilfe von strukturierten Gesprächen und ausgewählten Methoden begleite ich Sie dabei, in einem geschützten Rahmen eigene Lösungen zu entwickeln und umzusetzen.</p>
    </div>
    <div class="abs info" style="top:148px">
      <h3 class="h-green">Geht es nur um berufliche Themen?</h3>
      <p>Nein. Private Themen können Kraftgeber und Krafträuber sein und sich auf berufliche Themen auswirken. Es geht oft um die Balance im Leben und deshalb ist es gut beides im Auge zu haben. Coaching ist aber keine Therapie.</p>
    </div>
    <h3 class="abs info h-orange serif" style="top:278px;font-weight:400;font-size:12px">Häufige Themenfelder:</h3>
    <div class="abs tiles">
      <div class="tile tile--dark"><b>Berufliche Kompetenzen</b>Führung, Umgang mit Veränderungen, herausfordernde Aufgaben meistern</div>
      <div class="tile tile--light"><b>Persönlichen Kompetenzen</b>neue Perspektiven, Work-Life-Balance, Konfliktverhalten</div>
      <div class="tile tile--light"><b>Team</b>Zusammenarbeit, Kommunikation, Konflikte</div>
      <div class="tile tile--light"><b>Supervisorische Fallarbeit</b>schwierige Fälle/ Klienten</div>
    </div>
  </article>

  <article class="panel approach">
    <h2 class="abs mean-title serif" style="font-weight:500">Coaching &amp; Supervision bedeutet für mich:</h2>
    <div class="abs chips">
      <span class="chip">Ressourcen<br>stärken</span>
      <span class="chip">an Heraus-<br>forderungen wachsen</span>
      <span class="chip">das Leben<br>gestalten</span>
      <span class="chip">sich (weiter)<br>entwickeln</span>
    </div>
    <div class="img sprout" role="img" aria-label="Junge Keimlinge und eine gelbe Blüte im Erdreich"></div>
    <div class="abs attitude">
      <h4>Meine<br>Grundhaltung:</h4>
      <ul>
        <li>systemisch</li>
        <li>lösungs- und zielorientiert</li>
        <li>ressourcen-orientiert</li>
        <li>wertschätzend</li>
      </ul>
    </div>
    <div class="abs tmpl">
      <h3>Ich habe keine „Beratungsschablonen“.</h3>
      <p>Mir ist wichtig, mit welcher Arbeitsmethode Sie sich wohlfühlen. Deshalb passe ich die Methoden situativ Ihren Bedürfnissen an. Dazu bringe ich einen großen Methodenschatz mit. Besonders wichtig ist mir der Transfer in den Alltag.</p>
    </div>
    <div class="abs answer"></div>
    <div class="abs answer-txt">
      <h3>Die Antwort auf<br>Ihre Frage liegt schon<br>in Ihnen…</h3>
      <p>… ich helfe Ihnen, sie zu sehen. Und manchmal helfe ich auch, sich erstmal über die Frage klar zu werden.</p>
    </div>
    <div class="img portrait" role="img" aria-label="Porträtfoto der Psychologin in heller Bluse"></div>
  </article>
</section>

</body>
</html>
```